Design a CLEAN but CREATIVE Business Card (MULTIPLE WINNERS)

***WE WILL SELECT UP TO 10 WINNERS!***
****Use attached template****300dpi CMYK - Layered PSD file(s) needed at handover****

Use attached jpg file '[login to view URL]' and '[login to view URL]' as you want. You can also use different DNA image that you may like better.

This business card is targeted to OLDER people (55+) so designs should be nice and creative but still clean and simple. Here is the info (do NOT include {message in brackets} ) :

BACK -
nice design work

{MAIN HEADLINE}
Genetic Cancer Screening

{MESSAGE}
Identify if you have cancer causing genes. If detected, your provider can create a tailor made personal care plan to help reduce your risk.

NO COST IF YOU QUALIFY!

Lifegard and Statebrace may cover the full cost for genetic testing if:
•You have multiple members of your family who have or had cancer
•You currently have cancer or had cancer

Want to learn more? Watch the video at [login to view URL]

FRONT -
Use logo

nice design work

Marcus Feld
555-301-6492
mfeld@[login to view URL]

```html
<!DOCTYPE html>
<html lang="en">
<head>
<meta charset="utf-8">
<title>C.G.S Business Card</title>
<link href="https://fonts.googleapis.com/css2?family=Open+Sans:wght@400;600;700&family=Montserrat:wght@700&display=swap" rel="stylesheet">
<style>
  :root {
    --stage: #1d1d1f;
    --red: #e0321f;
    --red-deep: #c8261a;
    --ink: #2a2a2a;
    --paper: #f1f1f1;
    --paper-shade: #d9d9d9;
    --white: #ffffff;
    --skin-light: #efe2d6;
    --skin-mid: #d9b8a2;
  }
  * { box-sizing: border-box; margin: 0; padding: 0; }
  html, body { width: 1200px; height: 821px; overflow: hidden; }
  body {
    background: var(--stage);
    font-family: "Open Sans", sans-serif;
    display: flex; flex-direction: column; align-items: center; justify-content: center; gap: 36px;
  }
  .card {
    position: relative; width: 620px; height: 354px; overflow: hidden;
    box-shadow: 0 10px 30px rgba(0,0,0,.5);
  }

  /* Back */
  .card-back { background: var(--paper); }
  .back-photo {
    position: absolute; inset: 0;
    background: linear-gradient(100deg, #cfcfcf 0%, #e6ddd5 35%, var(--skin-light) 60%, var(--skin-mid) 100%);
  }
  .back-veil { position: absolute; inset: 0; background: rgba(255,255,255,.35); }
  .back-content {
    position: relative; height: 100%; padding: 28px 34px 0 150px;
    display: flex; flex-direction: column; align-items: center; text-align: center; color: var(--ink);
  }
  .brand-name { font-family: "Montserrat", sans-serif; font-weight: 700; color: var(--ink); line-height: 1; }
  .back-content .brand-name { font-size: 34px; letter-spacing: 1px; }
  .brand-tag { font-size: 9px; letter-spacing: 3px; text-transform: uppercase; margin-top: 4px; color: var(--ink); }
  .pill {
    display: inline-block; background: var(--red); color: var(--white);
    font-weight: 700; font-size: 14px; text-transform: uppercase;
    padding: 3px 14px; border-radius: 14px; margin: 14px 0 8px;
  }
  .back-copy { font-size: 13px; line-height: 1.45; }
  .criteria { list-style: none; font-size: 13px; line-height: 1.45; }
  .criteria li::before {
    content: ""; display: inline-block; width: 6px; height: 6px; border-radius: 50%;
    background: var(--red); margin-right: 4px; vertical-align: middle;
  }

  /* Front */
  .card-front { background: linear-gradient(135deg, var(--white), var(--paper-shade)); }
  .front-shapes { position: absolute; inset: 0; }
  .front-brand {
    position: absolute; left: 70px; top: 120px; width: 210px; text-align: center;
  }
  .front-brand .brand-mark {
    width: 56px; height: 56px; border-radius: 50%; background: var(--red); margin: 0 auto 14px;
  }
  .front-brand .brand-name { font-size: 36px; letter-spacing: 1px; }
  .front-brand .brand-tag { font-size: 8px; }
  .contact { position: absolute; right: 40px; top: 70px; color: var(--white); text-align: right; }
  .contact-name { font-size: 26px; font-weight: 600; text-transform: uppercase; letter-spacing: .5px; }
  .contact-role { font-size: 14px; margin-top: 2px; }
  .contact-lines { list-style: none; margin-top: 50px; font-size: 15px; line-height: 1.55; }
  .contact-lines li { display: flex; align-items: center; justify-content: flex-end; gap: 8px; }
  .contact-lines svg { width: 14px; height: 14px; }
</style>
</head>
<body>

<section class="card card-back">
  <div class="back-photo" role="img" aria-label="Photo of a patient having a cheek swab taken for a DNA test"></div>
  <div class="back-veil"></div>
  <div class="back-content">
    <div class="brand-name">C.G.S</div>
    <div class="brand-tag">Clear Gene Solutions</div>
    <span class="pill">Genetic Cancer Screening</span>
    <p class="back-copy">Identify if you have cancer causing genes. If detected, your provider can create a tailor made personal care plan to help reduce your risk.</p>
    <span class="pill">No cost if you qualify!</span>
    <p class="back-copy">Lifegard and Statebrace may cover the full cost for genetic testing if:</p>
    <ul class="criteria">
      <li>You have multiple members of your family who have or had cancer</li>
      <li>You currently have cancer or had cancer</li>
    </ul>
  </div>
</section>

<section class="card card-front">
  <svg class="front-shapes" viewBox="0 0 620 354" preserveAspectRatio="none">
    <polygon points="330,0 620,0 620,354 410,354" fill="var(--red)"/>
    <polygon points="300,0 340,0 420,354 380,354" fill="var(--red-deep)" role="img" aria-label="Colourful DNA double helix illustration"/>
  </svg>
  <div class="front-brand">
    <div class="brand-mark"></div>
    <div class="brand-name">C.G.S</div>
    <div class="brand-tag">Clear Gene Solutions</div>
  </div>
  <div class="contact">
    <div class="contact-name">Marcus Feld</div>
    <div class="contact-role">Director</div>
    <ul class="contact-lines">
      <li>555-301-6492
        <svg viewBox="0 0 14 14"><rect x="3.5" y="1" width="7" height="12" rx="1.5" fill="none" stroke="#fff" stroke-width="1.4"/><circle cx="7" cy="11" r=".8" fill="#fff"/></svg></li>
      <li>mfeld@cgsmail.com
        <svg viewBox="0 0 14 14"><rect x="1" y="3" width="12" height="8" fill="#fff"/><path d="M1 3l6 5 6-5" fill="none" stroke="var(--red)" stroke-width="1.2"/></svg></li>
      <li>www.cgs.video/mfeld
        <svg viewBox="0 0 14 14"><circle cx="7" cy="7" r="5.8" fill="none" stroke="#fff" stroke-width="1.3"/><ellipse cx="7" cy="7" rx="2.5" ry="5.8" fill="none" stroke="#fff" stroke-width="1"/><path d="M1.5 7h11" stroke="#fff" stroke-width="1"/></svg></li>
    </ul>
  </div>
</section>

</body>
</html>
```